Female Focused - Finance Company needs a website

I need a website for a new company based in London called 'Lorinda Pelham Associates'. The company has been set up with a focus on empowering creativity and encouraging women to engage with finance and build their knowledge and understanding. I am targeting professional women and entrepreneurs in the late 20s to 40s age bracket. The mission is to empower women to achieve financial independence and inspire community and connectivity. I want to create a brand that promotes financial security, growth and connectivity.

The website at this stage can be relatively simple, I just want to be able to have a section about me and the work that I do, have contact details for people to be able to get in touch and find out more.

I run a series of different events and want to have a page whereby I can showcase the events that I am running. They can also use links to click through and register for events. I also want to be able to put images up of previous events that I have run. Maybe having a calendar on the website of different things that are happening.

I am creating a membership club called Hop3Hop and I want to have a page whereby they can find out about the membership and the different options that are available.

I have attached the logo below so you can see the designs so far.

I also own the domain name lorindapelhamassociates.com

```html
<!DOCTYPE html>
<html lang="en">
<head>
<meta charset="utf-8">
<title>Lorinda Pelham Associates</title>
<link rel="stylesheet" href="https://fonts.googleapis.com/css2?family=Montserrat:wght@400;500;600&display=swap">
<style>
:root{
  --ink:#111111;
  --white:#ffffff;
  --btn:#555456;
  --mist:#f1f1f1;
  --night:#000000;
  --line:#333333;
  --muted:#555555;
}
*{margin:0;padding:0;box-sizing:border-box}
html,body{width:695px;height:1200px;overflow:hidden;background:var(--white)}
body{font-family:"Montserrat",sans-serif;color:var(--ink);position:relative}
.abs{position:absolute}

/* header */
.site-header{position:absolute;left:0;top:0;width:695px;height:82px;background:var(--white)}
.brand{position:absolute;left:88px;top:18px;display:flex;align-items:center;gap:5px}
.brand-dot{width:10px;height:10px;border:1px solid var(--ink);border-radius:50%}
.brand-name{font-size:7px;font-weight:500;line-height:1.2;width:70px}
.nav a{position:absolute;top:37px;font-size:7.4px;font-weight:500;color:var(--ink);text-decoration:none;letter-spacing:.1px}
.nav .member{display:flex;align-items:center;gap:2px;top:35px}
.btn{position:absolute;background:var(--btn);color:var(--white);font-size:7px;font-weight:500;display:flex;align-items:center;justify-content:center;letter-spacing:.2px;box-shadow:1px 1px 0 rgba(0,0,0,.15)}

/* hero */
.hero{position:absolute;left:0;top:82px;width:695px;height:330px;
  background:linear-gradient(180deg,#5c4a38 0%,#5f4e33 35%,#6a3d1c 62%,#3a1a08 78%,#000 88%)}
.hero-sub{position:absolute;top:185px;width:695px;text-align:center;color:var(--white);font-size:9.6px}
.hero-title{position:absolute;top:205px;width:695px;text-align:center;color:var(--white);font-size:30px;line-height:38px;font-weight:600}
.hero-title .light{font-weight:400}
.hero-curve{position:absolute;left:0;top:0}

/* about */
.mark{position:absolute;left:110px;top:470px;width:156px;height:156px;border:1.3px solid var(--ink);border-radius:50%;display:flex;align-items:center;justify-content:center}
.mark-name{font-size:11px;font-weight:500;text-align:center;line-height:1.35}
.tagline{position:absolute;left:90px;top:657px;font-size:9.6px;letter-spacing:4.3px;color:var(--muted)}
.about-kicker{position:absolute;left:352px;top:443px;font-size:9.6px}
.about-name{position:absolute;left:352px;top:464px;font-size:16px;font-weight:600;color:#222}
.about-copy{position:absolute;left:352px;top:498px;width:262px;font-size:7.5px;line-height:14px}

/* contact */
.contact-bg{position:absolute;left:0;top:700px}
.contact-title{position:absolute;top:760px;width:695px;text-align:center;font-size:18px;font-weight:500}
.info{position:absolute;left:74px;display:flex;gap:5px}
.info-icon{width:23px;height:23px;border:1px solid var(--ink);border-radius:50%;display:flex;align-items:center;justify-content:center;margin-top:1px}
.info-text{font-size:7.6px;line-height:10px;padding-top:1px}
.info-text b{font-weight:500;display:block}
.field{position:absolute;left:339px;width:230px;background:var(--white);border:0.8px solid var(--line);font-size:7.4px;color:#777;padding:9px 8px}

/* footer */
.site-footer{position:absolute;left:0;top:1061px;width:695px;height:139px;background:var(--night);color:var(--white)}
.footer-links a{position:absolute;top:35px;font-size:7.6px;color:var(--white);text-decoration:none}
.copyright{position:absolute;top:62px;width:695px;text-align:center;font-size:7.6px}
.social{position:absolute;top:96px;width:17px;height:17px;border:1.6px solid var(--white);border-radius:50%}
</style>
</head>
<body>

<header class="site-header">
  <div class="brand">
    <span class="brand-dot"></span>
    <span class="brand-name">Lorinda Pelham Associates</span>
  </div>
  <nav class="nav">
    <a style="left:283px">HOME</a>
    <a style="left:330px">ABOUT</a>
    <a style="left:381px">EVENT</a>
    <a class="member" style="left:432px">
      <svg width="11" height="11" viewBox="0 0 12 12" fill="none" stroke="#111" stroke-width="1"><circle cx="6" cy="3.6" r="2.6"/><path d="M1 11.5c0-3 2.2-4.6 5-4.6s5 1.6 5 4.6z"/></svg>
      MEMBER ACCESS
    </a>
  </nav>
  <a class="btn" style="left:532px;top:28px;width:90px;height:27px">LET’S MEET</a>
</header>

<section class="hero" role="img" aria-label="Photo of women holding hands in silhouette against a sunset sky">
</section>
<svg class="hero-curve" width="695" height="420" viewBox="0 0 695 420">
  <path d="M0 374 Q347 436 695 375 L695 420 L0 420 Z" fill="#ffffff"/>
</svg>
<p class="hero-sub">Lorinda Pelham Associates</p>
<h1 class="hero-title">Empowering<br>Woman <span class="light">Creativity</span></h1>

<section class="about">
  <div class="mark"><span class="mark-name">Lorinda Pelham<br>Associates</span></div>
  <p class="tagline">EMPOWERING CREATIVITY</p>
  <p class="about-kicker">About Me</p>
  <h2 class="about-name">Lorinda Pelham</h2>
  <p class="about-copy">Lorem ipsum dolor sit amet consectetur. Sit pellentesque ut eu et id praesent quam. Purus at amet sed tempor. Cras in augue amet facilisi id ornare ultrices in. Consequat in accumsan ut ullamcorper. Diam facilisis fringilla leo parturient ac purus leo massa faucibus. Tincidunt praesent sollicitudin luctus id nec netus. Libero turpis sit malesuada purus non sed. Elementum mauris lacus eget viverra in amet lectus lacus varius. Vel viverra imperdiet egestas tellus urna. Lacus interdum platea magna posuere. Diam gravida mauris enim semper scelerisque bibendum libero.</p>
  <a class="btn" style="left:350px;top:642px;width:89px;height:27px">LET’S MEET</a>
</section>

<section class="contact">
  <svg class="contact-bg" width="695" height="361" viewBox="0 0 695 361">
    <path d="M0 34 C200 28 330 10 440 9 C560 8 640 22 695 34 L695 361 L0 361 Z" fill="#f1f1f1"/>
  </svg>
  <h2 class="contact-title">Contact Us</h2>

  <div class="info" style="top:824px">
    <span class="info-icon"><svg width="10" height="11" viewBox="0 0 10 11" fill="none" stroke="#111" stroke-width="0.9"><path d="M5 10.3C2.6 7.8 1.4 5.9 1.4 4.3a3.6 3.6 0 0 1 7.2 0c0 1.6-1.2 3.5-3.6 6z"/><circle cx="5" cy="4.3" r="1.3"/></svg></span>
    <div class="info-text"><b>Location</b>Lorem ipsum dolor sit<br>amet consectetur. Sit.</div>
  </div>
  <div class="info" style="top:879px">
    <span class="info-icon"><svg width="10" height="11" viewBox="0 0 10 11" fill="none" stroke="#111" stroke-width="0.9"><path d="M5 10.3C2.6 7.8 1.4 5.9 1.4 4.3a3.6 3.6 0 0 1 7.2 0c0 1.6-1.2 3.5-3.6 6z"/><circle cx="5" cy="4.3" r="1.3"/></svg></span>
    <div class="info-text"><b>Phone</b>+888 8888 888</div>
  </div>
  <div class="info" style="top:926px">
    <span class="info-icon"><svg width="10" height="11" viewBox="0 0 10 11" fill="none" stroke="#111" stroke-width="0.9"><path d="M5 10.3C2.6 7.8 1.4 5.9 1.4 4.3a3.6 3.6 0 0 1 7.2 0c0 1.6-1.2 3.5-3.6 6z"/><circle cx="5" cy="4.3" r="1.3"/></svg></span>
    <div class="info-text"><b>Email</b>info@lorindapelhamassociates.com</div>
  </div>

  <div class="field" style="top:811px;height:27px;box-shadow:0 1px 2px rgba(0,0,0,.25)">Name</div>
  <div class="field" style="top:849px;height:27px">Phone</div>
  <div class="field" style="top:890px;height:27px">Email</div>
  <div class="field" style="top:925px;height:53px">Message</div>
  <a class="btn" style="left:339px;top:992px;width:89px;height:26px">SUMBIT</a>
</section>

<footer class="site-footer">
  <nav class="footer-links">
    <a style="left:244px">Terms &amp;Conditions</a>
    <a style="left:347px">Privacy Policy</a>
    <a style="left:436px">About</a>
  </nav>
  <p class="copyright">Copyrights 2023 Lorinda Pelham Asssociates All Rights Reserved</p>
  <span class="social" style="left:308px" aria-label="Social link"></span>
  <span class="social" style="left:339px" aria-label="Social link"></span>
  <span class="social" style="left:370px" aria-label="Social link"></span>
</footer>

</body>
</html>
```